Creative lead conversion landing page for SMBs

We have an AI chatbot webpage for a real estate agent, and we’re are going to start sending traffic to that webpage (primarily from Zorvane)
We want to maximize the percentage of visitors who start conversations with the chatbot.
We have a specific area of the webpage where we can include any HTML.
We need the design and HTML for both desktop and mobile version.
We’re looking for the best designs that help convert visitors into people who engage the chatbot.

Details are in the attached document "Artquilly project for chat conversion". Please let me know if you have any questions!

Target Market(s)

SMBs (think real estate agents, or home services like tree care, housekeepers, electricians, general contractors) will be selling to consumers

Number of Pages Required

1 page

Font styles to use
Other font styles liked:
• Zorvane Poppins

Requirements
Must have
• Creative design that catches users eyes and with good content (content of course out of scope) will encourage a user to want to learn more.

```html
<!DOCTYPE html>
<html lang="en">
<head>
<meta charset="utf-8">
<title>Hey Mabel! – Marisa, Real Estate Agent</title>
<link href="https://fonts.googleapis.com/css2?family=Poppins:ital,wght@0,400;0,500;0,600;0,700;0,800;1,400&display=swap" rel="stylesheet">
<style>
  :root {
    --purple: #6457a6;
    --navy: #021830;
    --teal: #21b3d4;
    --sidebar: #f1f1f1;
    --white: #ffffff;
    --text: #555a63;
    --heading: #0e1b2c;
    --online: #13c12a;
    --star: #f7a600;
    --input: #ececec;
    --muted: #9aa0a8;
  }
  * { box-sizing: border-box; margin: 0; padding: 0; }
  html, body { width: 1152px; height: 1200px; overflow: hidden; }
  body { font-family: "Poppins", sans-serif; background: var(--white); position: relative; color: var(--text); }

  .sidebar { position: absolute; left: 0; top: 0; width: 314px; height: 1110px; background: var(--sidebar); }
  .brand-bar { height: 68px; background: var(--purple); display: flex; align-items: center; justify-content: center; }
  .brand-bar .brand { color: var(--white); font-weight: 700; font-size: 27px; }

  .avatar { position: absolute; left: 84px; top: 108px; width: 146px; height: 146px; border: 1.5px solid var(--online); border-radius: 50%; }
  .avatar .photo { position: absolute; inset: 5px; border-radius: 50%; background: radial-gradient(circle at 55% 55%, #c9a28d 0%, #7a5a4c 45%, #2a211e 100%); }
  .avatar .status { position: absolute; left: 102px; top: 122px; width: 20px; height: 20px; border-radius: 50%; background: var(--online); border: 2px solid var(--white); }

  .agent-name { position: absolute; top: 268px; width: 314px; text-align: center; font-weight: 700; font-size: 28px; color: var(--heading); }
  .agent-role { position: absolute; top: 305px; width: 314px; text-align: center; font-size: 17px; color: var(--text); }
  .agent-bio { position: absolute; top: 335px; left: 47px; width: 220px; text-align: center; font-size: 12px; line-height: 20px; color: var(--text); }

  .review-card { position: absolute; left: 30px; top: 437px; width: 252px; height: 141px; background: var(--white); border-radius: 9px; box-shadow: 0 2px 10px rgba(0,0,0,0.07); padding: 18px 19px; }
  .stars { display: flex; gap: 3px; }
  .review-quote { margin-top: 6px; font-style: italic; font-size: 12px; line-height: 20px; color: var(--text); }
  .review-author { margin-top: 6px; font-weight: 600; font-size: 12.5px; color: var(--heading); }

  .carousel-dots { position: absolute; top: 596px; left: 0; width: 314px; display: flex; justify-content: center; gap: 6px; }
  .carousel-dots span { width: 8px; height: 2.5px; background: #c7c7c7; border-radius: 2px; }
  .carousel-dots span.active { width: 26px; background: var(--purple); }

  .assistant-prompt { position: absolute; top: 634px; width: 314px; text-align: center; font-weight: 500; font-size: 14.5px; color: var(--teal); }
  .pill { position: absolute; left: 31px; width: 251px; height: 42px; border-radius: 21px; display: flex; align-items: center; justify-content: center; color: var(--white); font-weight: 700; font-size: 13.5px; }
  .pill-search { top: 668px; background: var(--navy); }
  .pill-things { top: 725px; background: var(--purple); }
  .pill-review { top: 782px; background: var(--teal); }

  .chat { position: absolute; left: 314px; top: 0; width: 838px; height: 1110px; }
  .bubble { position: absolute; background: var(--white); border-radius: 9px; box-shadow: 0 2px 10px rgba(0,0,0,0.08); font-size: 15px; line-height: 26px; color: var(--text); padding: 14px 19px; }
  .bubble-bot-1 { left: 33px; top: 649px; width: 408px; height: 131px; }
  .bubble-bot-2 { left: 33px; top: 854px; width: 408px; height: 84px; padding-top: 16px; }
  .bubble-tail { position: absolute; left: 84px; top: 936px; }
  .bubble-user { position: absolute; left: 668px; top: 797px; width: 140px; height: 42px; background: var(--purple); border-radius: 8px; color: var(--white); font-size: 15px; font-weight: 500; display: flex; align-items: center; justify-content: center; box-shadow: 0 3px 8px rgba(100,87,166,0.3); }
  .mascot { position: absolute; left: 34px; top: 948px; width: 56px; height: 70px; border-radius: 45% 45% 35% 35%; background: linear-gradient(180deg, #7fd6e4 0%, #3fb7cf 100%); }

  .composer { position: absolute; left: 18px; top: 1034px; width: 789px; height: 52px; background: var(--input); border-radius: 26px; display: flex; align-items: center; padding-left: 23px; }
  .composer .placeholder { font-size: 17px; color: var(--muted); }
  .send { position: absolute; right: 6px; top: 6px; width: 40px; height: 40px; border-radius: 50%; background: var(--purple); display: flex; align-items: center; justify-content: center; }

  .footer { position: absolute; left: 0; top: 1110px; width: 1152px; height: 90px; background: var(--navy); }
  .pill-create { top: 23px; background: var(--purple); }
  .footer-brand { position: absolute; right: 30px; top: 20px; text-align: right; }
  .footer-brand .brand { color: var(--white); font-weight: 700; font-size: 25px; line-height: 30px; }
  .footer-brand .disclaimer { color: var(--muted); font-size: 11px; margin-top: 2px; }
</style>
</head>
<body>
  <aside class="sidebar">
    <div class="brand-bar"><span class="brand">Hey Mabel!</span></div>

    <div class="avatar">
      <div class="photo" role="img" aria-label="Portrait photo of the agent"></div>
      <div class="status"></div>
    </div>

    <h1 class="agent-name">Marisa</h1>
    <p class="agent-role">Real Estate Agent</p>
    <p class="agent-bio">Lorem ipsum dolor sit amet, sectetur adipiscing elit, sed ist do eiusmod tempor incididunt ut labore et dolore magna aliqua.</p>

    <div class="review-card">
      <div class="stars">
        <svg width="68" height="11" viewBox="0 0 68 11">
          <g fill="#f7a600">
            <polygon points="5.5,0 7,3.8 11,4 7.9,6.6 9,10.5 5.5,8.3 2,10.5 3.1,6.6 0,4 4,3.8"/>
            <polygon transform="translate(14,0)" points="5.5,0 7,3.8 11,4 7.9,6.6 9,10.5 5.5,8.3 2,10.5 3.1,6.6 0,4 4,3.8"/>
            <polygon transform="translate(28,0)" points="5.5,0 7,3.8 11,4 7.9,6.6 9,10.5 5.5,8.3 2,10.5 3.1,6.6 0,4 4,3.8"/>
            <polygon transform="translate(42,0)" points="5.5,0 7,3.8 11,4 7.9,6.6 9,10.5 5.5,8.3 2,10.5 3.1,6.6 0,4 4,3.8"/>
            <polygon transform="translate(56,0)" points="5.5,0 7,3.8 11,4 7.9,6.6 9,10.5 5.5,8.3 2,10.5 3.1,6.6 0,4 4,3.8"/>
          </g>
        </svg>
      </div>
      <p class="review-quote">“Ut enim ad minim veniam, is quis nostrud exercitation ullamco laboris nisi ut aliquip ex ea commodo.”</p>
      <p class="review-author">- Owen Castell</p>
    </div>

    <div class="carousel-dots"><span></span><span></span><span class="active"></span><span></span><span></span><span></span></div>

    <p class="assistant-prompt">Talk To Mabel, My AI Assistant.</p>
    <div class="pill pill-search">Search For Real Estate</div>
    <div class="pill pill-things">Things To Do In Indianapolis</div>
    <div class="pill pill-review">My Review</div>
  </aside>

  <main class="chat">
    <div class="bubble bubble-bot-1">Hi! I'm the AI assistant to Marisa, who can help you buy or sell a home in the Indianapolis area. I am happy to help get you connected to her. First, what's your name?</div>
    <div class="bubble-user">Johnathan</div>
    <div class="bubble bubble-bot-2">Hi Johnathan! It's great to meet you. How can I assist you today?</div>
    <svg class="bubble-tail" width="32" height="26" viewBox="0 0 32 26"><polygon points="0,0 32,0 0,26" fill="#ffffff"/></svg>
    <div class="mascot" role="img" aria-label="Assistant bird mascot character"></div>

    <div class="composer">
      <span class="placeholder">Type Your Message...</span>
      <div class="send">
        <svg width="20" height="18" viewBox="0 0 20 18"><polygon points="0,0 20,9 0,18 3,9" fill="#ffffff"/></svg>
      </div>
    </div>
  </main>

  <footer class="footer">
    <div class="pill pill-create">Create Your Own Free Mabel</div>
    <div class="footer-brand">
      <div class="brand">Hey Mabel!</div>
      <div class="disclaimer">Mabel Uses AI and Can Make Mistakes</div>
    </div>
  </footer>
</body>
</html>
```